ALL TEXT GRAPHICS TM May 2025 for Instagram

We are looking for a series of social media graphics for Instagram (new size: 4:5 (1080 x 1350 pixels) ratio that are ALL TEXT. We want the following quotes below on each graphic; one quote per graphic. AND, In very small letters at the bottom of each graphic, add @TovaMarshOnline
The look and feel of these graphics should be complimentary to the color palette attached below; but keep them simple. But the design is up to you; at the end of this document, I provided various samples of all text graphics that I like as examples.
Target Market(s)
women looking to lose weight
Look and feel

```html
<!DOCTYPE html>
<html lang="en">
<head>
<meta charset="utf-8">
<title>All Text Graphics – Tova Marsh</title>
<link href="https://fonts.googleapis.com/css2?family=Charis+SIL:wght@400;700&display=swap" rel="stylesheet">
<style>
  :root {
    --board: #826475;
    --card-pink: #fdd2e7;
    --card-light: #fff4fa;
    --accent: #e3238e;
    --ink: #3b3538;
    --muted: #4a4448;
  }
  * { margin: 0; padding: 0; box-sizing: border-box; }
  html, body { width: 1200px; height: 608px; overflow: hidden; }
  body {
    background: var(--board);
    font-family: "Charis SIL", Georgia, serif;
    color: var(--ink);
    position: relative;
  }
  .card {
    position: absolute;
    width: 210px;
    height: 268px;
    background:
      radial-gradient(circle at 100% 0%, var(--card-light) 0, rgba(255,244,250,0) 45%),
      radial-gradient(circle at 100% 100%, var(--card-light) 0, rgba(255,244,250,0) 40%),
      var(--card-pink);
  }
  .card.alt {
    background:
      radial-gradient(circle at 50% 100%, var(--card-light) 0, rgba(255,244,250,0) 40%),
      radial-gradient(circle at 10% 0%, var(--card-light) 0, rgba(255,244,250,0) 40%),
      var(--card-pink);
  }
  .row-1 { top: 24px; }
  .row-2 { top: 316px; }
  .col-1 { left: 28px; }
  .col-2 { left: 262px; }
  .col-3 { left: 495px; }
  .col-4 { left: 729px; }
  .col-5 { left: 962px; }

  .block { position: absolute; left: 0; right: 0; text-align: center; padding: 0 8px; }
  .block.left { text-align: left; padding: 0 12px 0 26px; }
  .block.left.tight { padding: 0 4px 0 17px; }
  .nowrap { white-space: nowrap; }

  .headline { font-weight: 700; color: var(--accent); letter-spacing: 0.3px; }
  .body { color: var(--muted); }
  .accent { color: var(--accent); }
  .dark { color: var(--ink); }
  .bold { font-weight: 700; }
  .link { color: var(--accent); font-weight: 700; text-decoration: underline; text-underline-offset: 2px; text-decoration-thickness: 1px; }
  .handle { font-size: 8px; color: var(--muted); }

  .secret-box {
    position: absolute;
    left: 26px; top: 43px;
    width: 157px; height: 109px;
    border: 3px solid var(--accent);
    display: flex; align-items: center; justify-content: center;
    text-align: center;
    font-weight: 700; color: var(--accent);
    font-size: 14px; line-height: 17px; letter-spacing: 0.3px;
  }
</style>
</head>
<body>

<section class="card row-1 col-1">
  <h2 class="block headline" style="top:57px;font-size:29px;line-height:31px;">Flat tummy<br>in your 40s?</h2>
  <p class="block body" style="top:128px;font-size:14px;line-height:16px;">It’s still possible!<br>Comment <span class="accent bold">BYE BELLY</span></p>
  <p class="block body" style="top:169px;font-size:13px;line-height:16px;">To get the 10 SECRETS<br>to a flatter tummy</p>
  <p class="block handle" style="top:216px;">@TovaMarshOnline</p>
</section>

<section class="card alt row-1 col-2">
  <h2 class="block left headline" style="top:53px;font-size:21px;line-height:23px;">What worked in<br>your 30s <span class="dark">won’t<br>work now,</span></h2>
  <p class="block left body" style="top:130px;font-size:15px;line-height:17px;"><span class="link">Here’s what actually does.</span> Drop 30 Pounds in 3 Months.</p>
  <p class="block left handle" style="top:200px;">@TovaMarshOnline</p>
</section>

<section class="card row-1 col-3">
  <h2 class="block headline" style="top:71px;font-size:20px;line-height:23px;">Tired. Moody.<br>Stubborn Belly Fat.</h2>
  <p class="block body" style="top:119px;font-size:16px;line-height:19px;">Your hormones are<br>screaming for help!</p>
  <p class="block accent" style="top:162px;font-size:19px;line-height:22px;">Let’s fix that.</p>
  <p class="block handle" style="top:204px;">@TovaMarshOnline</p>
</section>

<section class="card alt row-1 col-4">
  <h2 class="block left headline" style="top:41px;font-size:21px;line-height:23px;">That stubborn<br>weight? It’s not<br>your fault.</h2>
  <p class="block left body" style="top:116px;font-size:16px;line-height:19px;">Your hormones<br>are to blame and<br>you’re not alone.</p>
  <p class="block left accent" style="top:185px;font-size:16px;line-height:19px;">But there is a fix.</p>
  <p class="block left handle" style="top:217px;">@TovaMarshOnline</p>
</section>

<section class="card row-1 col-5">
  <div class="secret-box">This is the secret<br>women over 40<br>are using to get<br>snatched,<br>without starving.</div>
  <p class="block body" style="top:164px;font-size:17px;line-height:20px;">Comment <span class="accent bold">SKINNY</span><br>to get the exact plan</p>
  <p class="block handle" style="top:223px;">@TovaMarshOnline</p>
</section>

<section class="card alt row-2 col-1">
  <h2 class="block headline" style="top:75px;font-size:20px;line-height:22px;">The stubborn belly<br>fat after 40?</h2>
  <p class="block body" style="top:127px;font-size:14px;line-height:16px;">It’s not about calories,<br>it’s about your hormones.</p>
  <p class="block accent bold" style="top:162px;font-size:14px;line-height:16px;">Here is the fix!</p>
  <p class="block handle" style="top:198px;">@TovaMarshOnline</p>
</section>

<section class="card row-2 col-2">
  <h2 class="block headline" style="top:68px;font-size:17px;line-height:23px;">Bloating. Muffin top.<br><span style="font-size:21px;">Puffy waistline.</span></h2>
  <p class="block body" style="top:122px;font-size:14px;line-height:18px;">Your body’s screaming for<br>a different kind of fix.</p>
  <p class="block link" style="top:160px;font-size:17px;line-height:20px;">Here it is</p>
  <p class="block handle" style="top:207px;">@TovaMarshOnline</p>
</section>

<section class="card alt row-2 col-3">
  <h2 class="block headline" style="top:57px;font-size:19px;line-height:22px;">This <span class="dark" style="font-size:22px;">90-day plan</span><br>helped women over<br>40 slim down,</h2>
  <p class="block body" style="top:131px;font-size:12px;line-height:14px;">Get a tiny waist and feel<br>sexy again.</p>
  <p class="block accent bold" style="top:167px;font-size:17px;line-height:20px;">You’re next.</p>
  <p class="block handle" style="top:207px;">@TovaMarshOnline</p>
</section>

<section class="card row-2 col-4">
  <h2 class="block left tight headline nowrap" style="top:64px;font-size:16px;line-height:21px;letter-spacing:0;">Your belly isn’t fat…<br>it’s hormonal.</h2>
  <p class="block left tight body nowrap" style="top:119px;font-size:13.5px;line-height:18px;">And here’s how to fix it.<br><span class="accent bold">Comment HORMONES</span><br>if nothing is working.</p>
  <p class="block left tight handle" style="top:192px;">@TovaMarshOnline</p>
</section>

<section class="card alt row-2 col-5">
  <h2 class="block headline" style="top:73px;font-size:19px;line-height:22px;">You’re doing all<br>the “right” things,</h2>
  <p class="block body dark" style="top:124px;font-size:15px;line-height:18px;">but your belly won’t go<br>down? <span class="accent bold">Here’s</span> what<br>you haven’t tried.</p>
  <p class="block handle" style="top:205px;">@TovaMarshOnline</p>
</section>

</body>
</html>
```